Graphic Design for a Info Card

We would like a graphic design for an info card . We would like the colours to correspond to our logo , you can add in the colours navy blue or yellow if you would like. We would like it to have the following information. We want something that really pops. We would like the size to be 4 1/2 x 6 .

ATTENTION!! Delivery Promo! Order from us on the @hopplemeals app or @marlinrunner app on FRIDAYS and receive a FREE Sample of our one of our meal prep meals in your bag!
DID YOU KNOW?! Meal Prep is another great service that we offer. Saving you time, promoting your health, and best of all providing a delicious lunch . You can find more info on our website www.brivoranpantry.example . All orders are available for delivery or pickup!

```html
<!DOCTYPE html>
<html lang="en">
<head>
<meta charset="utf-8">
<title>Brivoran Delivery Promo Card</title>
<link href="https://fonts.googleapis.com/css2?family=Bebas+Neue&family=Kaushan+Script&family=Montserrat:wght@400;700;800&family=Open+Sans:ital,wght@0,800;1,700;1,800&display=swap" rel="stylesheet">
<style>
  :root {
    --navy: #1b3a6e;
    --navy-deep: #142f5c;
    --teal: #1383ab;
    --yellow: #ffe019;
    --orange: #fbb21c;
    --pink: #ec1566;
    --pink-fold: #2b2b2b;
    --green: #8cc63f;
    --red: #e8222c;
    --white: #ffffff;
    --ink: #1b1b1b;
    --page: #eeeeee;
  }
  * { box-sizing: border-box; margin: 0; padding: 0; }
  html, body { width: 1200px; height: 1200px; overflow: hidden; background: var(--page); }
  .card {
    position: absolute; left: 180px; top: 40px; width: 840px; height: 1120px;
    overflow: hidden;
    background: linear-gradient(135deg, var(--navy-deep) 0%, var(--navy) 40%, var(--teal) 100%);
    font-family: "Montserrat", sans-serif;
  }
  .light-shaft { position: absolute; inset: 0; }
  .brand { position: absolute; left: 34px; top: 40px; width: 450px; }
  .brand-name {
    font-family: "Montserrat", sans-serif; font-weight: 800; font-size: 74px;
    line-height: 1; letter-spacing: 4px; color: var(--green);
  }
  .brand-tagline {
    margin-top: 14px; font-family: "Montserrat", sans-serif; font-weight: 700;
    font-size: 25px; color: var(--green); letter-spacing: -0.3px; white-space: nowrap;
  }
  .burst { position: absolute; left: 470px; top: 0; width: 370px; height: 205px; }
  .burst-type { position: absolute; left: 0; top: 0; width: 840px; height: 220px; }
  .burst-script { font-family: "Kaushan Script", cursive; font-size: 54px; fill: var(--red); }
  .burst-promo { font-family: "Montserrat", sans-serif; font-weight: 800; font-size: 29px; letter-spacing: 2px; fill: var(--red); }
  .headline {
    position: absolute; left: 44px; top: 176px; width: 780px;
    font-family: "Bebas Neue", sans-serif; font-size: 214px; line-height: 1;
    color: var(--white); transform: skewX(-12deg); letter-spacing: -2px;
    text-shadow: 0 18px 26px rgba(0,0,0,0.55); white-space: nowrap;
  }
  .bubble { position: absolute; left: 20px; top: 420px; width: 414px; height: 150px; }
  .bubble-text {
    position: absolute; left: 48px; top: 440px; font-family: "Bebas Neue", sans-serif;
    font-size: 76px; line-height: 1; transform: skewX(-10deg);
    background: linear-gradient(90deg, var(--yellow), var(--orange));
    -webkit-background-clip: text; background-clip: text; color: transparent;
    filter: drop-shadow(0 6px 6px rgba(0,0,0,0.45));
  }
  .benefits { position: absolute; left: 46px; top: 604px; width: 380px; list-style: none; }
  .benefits li {
    position: relative; padding-left: 28px; margin-bottom: 12px;
    font-size: 28px; line-height: 39px; color: var(--white); font-weight: 400;
  }
  .benefits svg { position: absolute; left: 0; top: 10px; }
  .phone {
    position: absolute; left: 463px; top: 398px; width: 302px; height: 532px;
    background: var(--white); border-radius: 40px;
  }
  .phone-screen {
    position: absolute; left: 27px; top: 55px; width: 249px; height: 403px;
    background: linear-gradient(90deg, var(--orange), var(--yellow)); border-radius: 6px;
  }
  .phone-button {
    position: absolute; left: 132px; top: 467px; width: 38px; height: 38px;
    border: 5px solid var(--yellow); border-radius: 50%;
  }
  .ribbons { position: absolute; left: 410px; top: 470px; width: 420px; height: 240px; }
  .ribbon-text {
    position: absolute; font-family: "Bebas Neue", sans-serif; color: var(--white);
    text-align: center; line-height: 0.98; text-shadow: 3px 3px 0 rgba(0,0,0,0.35);
  }
  .ribbon-order { left: 440px; top: 484px; width: 330px; font-size: 50px; }
  .ribbon-sample { left: 418px; top: 622px; width: 404px; font-size: 50px; }
  .app { position: absolute; left: 490px; width: 249px; text-align: center; color: var(--ink); }
  .app-name { font-family: "Open Sans", sans-serif; font-weight: 800; font-size: 20px; color: var(--navy); }
  .app-handle { font-family: "Open Sans", sans-serif; font-weight: 800; font-size: 15px; letter-spacing: 0.2px; }
  .app-marlin-name { top: 708px; }
  .app-marlin-handle { top: 752px; }
  .app-hopple-name { top: 783px; }
  .app-hopple-handle { top: 829px; }
  .web-pill {
    position: absolute; left: 34px; top: 960px; width: 497px; height: 52px; border-radius: 10px;
    background: linear-gradient(90deg, var(--orange), var(--yellow));
    display: flex; align-items: center; justify-content: center;
    font-family: "Open Sans", sans-serif; font-style: italic; font-weight: 800;
    font-size: 29px; color: var(--navy-deep); white-space: nowrap;
  }
  .footer-note {
    position: absolute; left: 36px; top: 1030px; width: 780px;
    font-family: "Open Sans", sans-serif; font-style: italic; font-weight: 800;
    font-size: 26.5px; color: var(--yellow); white-space: nowrap; letter-spacing: 0.4px;
  }
</style>
</head>
<body>
  <main class="card">
    <svg class="light-shaft" viewBox="0 0 840 1120" aria-hidden="true">
      <polygon points="840,250 840,1120 120,1120 440,560" fill="#1a8fb8" opacity="0.28"/>
    </svg>

    <header class="brand">
      <div class="brand-name">BRIVORAN</div>
      <div class="brand-tagline">HEALTHY KITCHEN &nbsp;|&nbsp; MEAL PREP</div>
    </header>

    <svg class="burst" viewBox="0 0 370 205" aria-hidden="true">
      <defs>
        <linearGradient id="burstFill" x1="0" y1="0" x2="1" y2="0">
          <stop offset="0" stop-color="#fbb21c"/><stop offset="1" stop-color="#ffe019"/>
        </linearGradient>
      </defs>
      <polygon points="150,0 370,0 370,168 330,160 308,205 272,150 226,182 212,138 118,158 168,112 70,100 160,72 0,48 158,40" fill="#111"/>
      <polygon points="158,0 370,0 370,150 326,142 306,180 270,132 228,160 216,122 150,136 182,102 110,92 176,70 60,50 170,38" fill="url(#burstFill)"/>
    </svg>

    <svg class="burst-type" viewBox="0 0 840 220">
      <text class="burst-script" x="728" y="82" text-anchor="middle" dominant-baseline="central" transform="rotate(30 728 82)">Delivery</text>
      <text class="burst-promo" x="708" y="118" text-anchor="middle" dominant-baseline="central" transform="rotate(30 708 118)">PROMO!</text>
    </svg>

    <h1 class="headline">ATTENTION!!</h1>

    <svg class="bubble" viewBox="0 0 414 150" aria-hidden="true">
      <path d="M40,4 H370 Q410,4 410,50 V70 Q410,112 370,112 H240 L66,144 L170,112 H40 Q4,112 4,70 V50 Q4,4 40,4 Z"
            fill="#132a52" fill-opacity="0.35" stroke="#fff" stroke-width="4" stroke-linejoin="round"/>
    </svg>
    <div class="bubble-text">DID YOU KNOW?</div>

    <ul class="benefits">
      <li><svg width="24" height="22" viewBox="0 0 24 22" aria-hidden="true"><path d="M2,12 L9,19 L22,2" fill="none" stroke="#fff" stroke-width="2.5"/></svg>Meal Prep is another great service that we offer.</li>
      <li><svg width="24" height="22" viewBox="0 0 24 22" aria-hidden="true"><path d="M2,12 L9,19 L22,2" fill="none" stroke="#fff" stroke-width="2.5"/></svg>Saving you time, promoting your health, and best of all providing a delicious lunch.</li>
    </ul>

    <div class="phone">
      <div class="phone-screen"></div>
      <div class="phone-button"></div>
    </div>

    <svg class="ribbons" viewBox="0 0 420 240" aria-hidden="true">
      <polygon points="75,124 340,124 420,150 38,148" fill="var(--pink-fold)"/>
      <polygon points="30,0 374,2 356,124 24,116" fill="var(--pink)"/>
      <polygon points="20,138 420,146 404,230 2,222" fill="var(--pink)"/>
    </svg>
    <div class="ribbon-text ribbon-order">ORDER FROM US ON<br>FRIDAYS</div>
    <div class="ribbon-text ribbon-sample">RECEIVE A FREE SAMPLE</div>

    <div class="app app-name app-marlin-name">Marlin Runner</div>
    <div class="app app-handle app-marlin-handle">@MARLINRUNNER APP</div>
    <div class="app app-name app-hopple-name">Hopple</div>
    <div class="app app-handle app-hopple-handle">@HOPPLEMEALS APP</div>

    <div class="web-pill">www.brivoranpantry.example</div>
    <p class="footer-note">ALL ORDERS ARE AVAILABLE FOR DELIVERY OR PICKUP!</p>
  </main>
</body>
</html>
```